QUORVIX - Sydney Based Technology Consultancy -Logo & Business Card design

Who are we?
-
Quorvix is an emerging and advanced technology consulting and professional services business based in Sydney, Australia. Quorvix specialising in increasing value to organisations through the effective use of current and emerging technologies, ensuring that technology is a sustainable catalyst to attaining stated business goals.

We pride ourselves in challenging the norm.

What do we want?
-
We are looking to update our "Brand" we already have a simple “home grown” logo and we are now looking for a new one, once we have this updated logo and businesses look and feel though the business card design we will refresh our website with the new logo and design thus updating the Companies overall look at feel.

Our current site is www.quorvix-example.net.au is a very basic wordpress site and we will be updating it once we have the new logo and designs done

Our initial thoughts on the new Quorvix identity are
• Logo Concept
- One of the key things is obviously the 8
- I was thinking that a logo that had 8 as the core of the logo would be cool,
- Almost like having a “ring” or hoop that is twisted to form an 8 with different services scribed on the inside.
- So we would have a Large 8 and the inside would have ring each service or section engraved.

• Brand / web Feel
- Simple
- Professional
- Innovative
- Clear
- Destination
- Unique
- Impartial
- Safe
- Leading edge
- Familiar

- Emerging technologies
- White and ice / glacier blue
- The familiar feel of the Brindle web site
- Embedded specialist Video clips

• Portfolio of Services
- Quorvix – A smart place for Smart people
- Quorvix – we provide the process to take ideas from awareness to reality
- Focus should be on the brand quality consistent clear local knowledge with regional, national, theatre and global presence

Access to Specialists
- Emerging technologies
- Sustainability
- Collaboration
- Data centre
- Virtualisation

• Adjacent ideas under the one Brand
- Tembrosk – Enable Business Collaboration
- Plinsk – Infrastructure Virtualisation
- morvo - smart people and processes
- skandel - Emerging technologies
- brunhavel - business to technology integration
- tolpin - Smart Infrastructure
- yusk – Connected communities
- dwol - sustainability

Target Market(s)

Australia, New Zealand and Asia pacific organisations that are typically English speaking.
Markets
- IT & Technology partners
- Banking and Finance
- Health

Industry/Entity Type

Business

Requirements
Must have
• Logo
Business cards
Colour pallette
3D Logo
Nice to have
• Style guide
Designer who can also assist with new Wordpress design
Should not have
• we don't want cheap looking, overtly flashy or gimmicky logo.

```html
<!DOCTYPE html>
<html lang="en">
<head>
<meta charset="utf-8">
<title>Quorvix Business Card</title>
<link rel="stylesheet" href="https://fonts.googleapis.com/css2?family=Roboto+Condensed:wght@300&family=Kaushan+Script&family=Arimo:wght@400&display=swap">
<style>
  :root {
    --backdrop: #3a3a3a;
    --card: #050505;
    --wordmark: #7b7b7b;
    --rule: #d9d9d9;
    --text: #f2f2f2;
    --text-soft: #cfcfcf;
  }
  * { margin: 0; padding: 0; box-sizing: border-box; }
  html, body {
    width: 1200px;
    height: 1200px;
    overflow: hidden;
    background: var(--backdrop);
  }
  .canvas {
    position: relative;
    width: 1200px;
    height: 1200px;
  }
  .card {
    position: absolute;
    left: 256px;
    width: 675px;
    height: 403px;
    background: var(--card);
    box-shadow: 0 6px 18px rgba(0,0,0,0.55);
    overflow: hidden;
  }
  .card--front { top: 184px; }
  .card--back { top: 623px; }

  .rule {
    position: absolute;
    height: 2px;
    background: linear-gradient(90deg, transparent, var(--rule) 50%, transparent);
  }
  .card--front .rule { left: 252px; width: 172px; }
  .card--front .rule--top { top: 112px; }
  .card--front .rule--bottom { top: 289px; }
  .card--back .rule { left: 0; width: 675px; }
  .card--back .rule--top { top: 117px; }
  .card--back .rule--bottom { top: 286px; }

  .wordmark {
    position: absolute;
    left: 0; right: 0;
    top: 158px;
    text-align: center;
    font-family: "Roboto Condensed", "Arial Narrow", sans-serif;
    font-weight: 300;
    font-size: 96px;
    line-height: 96px;
    letter-spacing: 2px;
    color: var(--wordmark);
  }

  .identity {
    position: absolute;
    right: 328px;
    top: 176px;
    text-align: right;
    color: var(--text);
  }
  .identity__name {
    font-family: "Kaushan Script", cursive;
    font-size: 21px;
    line-height: 24px;
  }
  .identity__role {
    font-family: "Arimo", Arial, sans-serif;
    font-size: 11px;
    line-height: 16px;
    color: var(--text-soft);
  }
  .divider {
    position: absolute;
    left: 359px;
    top: 181px;
    width: 1px;
    height: 44px;
    background: var(--text-soft);
  }
  .contact {
    position: absolute;
    left: 372px;
    top: 182px;
    list-style: none;
    font-family: "Arimo", Arial, sans-serif;
    font-size: 9.5px;
    line-height: 12.5px;
    color: var(--text-soft);
  }
  .address {
    position: absolute;
    left: 0; right: 0;
    top: 352px;
    text-align: center;
    font-family: "Arimo", Arial, sans-serif;
    font-size: 12px;
    color: var(--text-soft);
    word-spacing: 1px;
  }
</style>
</head>
<body>
<main class="canvas">
  <section class="card card--front">
    <div class="rule rule--top"></div>
    <h1 class="wordmark">QUORVIX</h1>
    <div class="rule rule--bottom"></div>
  </section>

  <section class="card card--back">
    <div class="rule rule--top"></div>
    <div class="identity">
      <p class="identity__name">Maren Holt</p>
      <p class="identity__role">Marketing Director</p>
    </div>
    <div class="divider"></div>
    <ul class="contact">
      <li>Tel.: +61 2 9555 0142</li>
      <li>Fax: +61 2 9555 0187</li>
      <li>m.holt@quorvix-example.net.au</li>
    </ul>
    <div class="rule rule--bottom"></div>
    <p class="address">Harbour Lane . Pyrmont . NSW 2009 . AUSTRALIA</p>
  </section>
</main>
</body>
</html>
```